Brightwell Letterhead

We would like a letterhead for our company. I have uploaded our logo.

Brightwell Peak Consulting
1450 W Corvin Rd Ste 310
Fairhaven, OH 45099
844-555-0172

```html
<!DOCTYPE html>
<html lang="en">
<head>
<meta charset="utf-8">
<title>Brightwell Letterhead</title>
<link rel="stylesheet" href="https://fonts.googleapis.com/css2?family=Lato:wght@400;700&family=Montserrat:wght@400;700&family=Roboto+Condensed:wght@300;400&display=swap">
<style>
  :root {
    --teal: #155e6c;
    --green: #6cc49b;
    --ink: #555555;
    --ink-dark: #3c3c3c;
    --paper: #ffffff;
    --backdrop: #d7d7d7;
  }
  * { box-sizing: border-box; margin: 0; padding: 0; }
  html, body { width: 1056px; height: 1200px; overflow: hidden; }
  body { background: var(--backdrop); position: relative; }
  .letterhead {
    position: absolute; left: 103px; top: 0;
    width: 849px; height: 1200px;
    background: var(--paper);
    overflow: hidden;
  }
  .brand {
    position: absolute; left: 103px; top: 94px;
    display: flex; align-items: center; gap: 10px;
  }
  .brand-dot { width: 34px; height: 34px; border-radius: 50%; background: var(--teal); flex: none; }
  .brand-name {
    font-family: "Lato", sans-serif; font-weight: 700;
    font-size: 19px; color: var(--teal); letter-spacing: 1.2px;
    white-space: nowrap;
  }
  .contact {
    position: absolute; left: 569px; top: 60px;
    font-family: "Lato", sans-serif; font-size: 15px; line-height: 19px;
    color: var(--ink-dark); font-style: normal;
  }
  .contact-company { color: var(--teal); }
  .contact-lines { list-style: none; margin-top: 9px; }
  .contact-lines li { display: flex; align-items: center; gap: 14px; height: 24px; }
  .contact-lines svg { width: 16px; height: 14px; }
  .recipient { position: absolute; left: 103px; top: 348px; color: var(--ink); }
  .letter-date { font-family: "Montserrat", sans-serif; font-size: 18px; }
  .sender-name {
    font-family: "Montserrat", sans-serif; font-weight: 700;
    font-size: 29px; margin-top: 9px; letter-spacing: -0.3px;
  }
  .sender-title { font-family: "Montserrat", sans-serif; font-size: 18px; margin-top: 10px; }
  .letter-body {
    position: absolute; left: 103px; top: 502px; width: 643px;
    font-family: "Lato", sans-serif; font-size: 13.3px; line-height: 21.5px;
    letter-spacing: -0.2px;
    color: var(--ink); text-align: justify;
  }
  .letter-body p + p { margin-top: 20px; }
  .sign-off {
    position: absolute; left: 103px; top: 830px;
    font-family: "Roboto Condensed", sans-serif; font-size: 18px; color: var(--ink);
  }
  .signature {
    position: absolute; left: 103px; top: 886px;
    width: 92px; height: 42px;
    background: linear-gradient(90deg, rgba(21,94,108,0.25), rgba(21,94,108,0.1));
    border-radius: 4px;
  }
  .footer-band { position: absolute; left: 0; top: 1152px; width: 849px; height: 48px; }
  .website {
    position: absolute; left: 519px; top: 1158px;
    font-family: "Lato", sans-serif; font-size: 23px; letter-spacing: 1.6px;
    color: #ffffff;
  }
</style>
</head>
<body>
  <main class="letterhead">
    <header>
      <div class="brand">
        <span class="brand-dot"></span>
        <span class="brand-name">BRIGHTWELL PEAK CONSULTING</span>
      </div>
      <address class="contact">
        <div class="contact-company">Brightwell Peak Consulting</div>
        <div>1450 W Corvin Rd Ste 310</div>
        <div>Fairhaven, OH 45099</div>
        <ul class="contact-lines">
          <li>
            <svg viewBox="0 0 16 14" aria-hidden="true"><path d="M3 1 L6 4 L4.5 6 C5.5 8 7 9.5 9 10.5 L11 9 L14 12 L12 13.5 C6 13 2 8.5 1.5 3 Z" fill="var(--green)"/></svg>
            <span>844-555-0172</span>
          </li>
          <li>
            <svg viewBox="0 0 16 14" aria-hidden="true"><rect x="1" y="2" width="14" height="10" fill="var(--green)"/><path d="M1 2 L8 8 L15 2 M1 12 L6 7 M15 12 L10 7" stroke="#fff" stroke-width="1.2" fill="none"/></svg>
            <span>info@yourmail.com</span>
          </li>
        </ul>
      </address>
    </header>

    <section class="recipient">
      <div class="letter-date">01 December, 2021</div>
      <div class="sender-name">DANIEL HARTLEY</div>
      <div class="sender-title">Cheif Executive Officer</div>
    </section>

    <section class="letter-body">
      <p>Contrary to popular belief, Lorem Ipsum is not simply random text. It has roots in a piece of classical Latin literature from 45 BC, making it over 2000 years old. Richard Alderton, a Latin professor at Marlow Ridge College in Virginia, looked up one of the more obscure Latin words, consectetur. The standard chunk of Lorem Ipsum used since the 1500s is reproduced below for those interested.</p>
      <p>Lorem Ipsum comes from sections 1.10.32 and 1.10.33 of "de Finibus Bonorum et Malorum" (The Extremes of Good and Evil) by Aurelian, written in 45 BC. This book is a treatise on the theory of ethics, very popular during the Renaissance. The first line of Lorem Ipsum.This book is a treatise on the theory of ethics, very popular during the Renaissance. The first line of Lorem Ipsum.</p>
      <p>The standard chunk of Lorem Ipsum used since the 1500s is reproduced below for those interested. This book is a treatise on the theory of ethics, very popular during the Renaissance. The first line of Lorem Ipsum. The first line of Lorem Ipsum.This book is a treatise on the theory of ethics, very popular during the Renaissance.</p>
    </section>

    <div class="sign-off">Best Regards</div>
    <div class="signature" role="img" aria-label="Handwritten signature of the sender"></div>

    <footer>
      <svg class="footer-band" viewBox="0 0 849 48" preserveAspectRatio="none" aria-hidden="true">
        <path d="M0 13 H440 C428 20 418 25 400 25 H0 Z" fill="var(--green)"/>
        <path d="M0 33 H405 C440 33 452 0 495 0 H849 V48 H0 Z" fill="var(--teal)"/>
      </svg>
      <div class="website">www.yourwebsite.com</div>
    </footer>
  </main>
</body>
</html>
```